Industry leading Property Management Company needs a flyer!

We need a brochure describing our fees and a basic description of what we do. This brochure will be printed, to be given to prospective clients, but we would also like an electronic version that can be downloaded from our website as a PDF. This project will be printed double sided, on standard 8.5" x 11" paper, in landscape mode, as a tri-fold brochure.

Target Market(s)

Real estate investors, but more importantly, first time investors. Many of our clients are "accidental landlords" who had their property for sale that didn't sell, so they are trying property management and rental investing for the first time. TRUST is their biggest fear

Font styles to use
Sans Serif

Requirements
Must have
• Must incorporate our logo, elements of our pricing list, and incorporate the text from our home page and "property management info" page (www.corvalinkrent.net). A word document specifying this text has been included in the project brief.
• Additionally, I am thinking this will be a simple, single piece of paper, in landscape mode, printed on both sides, in a Tri-fold. The front of the brochure will have the logo/name of the company, along with the Harbor Tenant Medals logos. I am thinking the first inside pane, when someone opens up the brochure, will have reference text #1 and #3. The 3 tiered pricing plan might occupy the 2nd and 3rd of the three panes on the inside fold. Reference text #4, 5, and 6 will occupy the next pane (see brief for handwritten layout). Then, the very back pane (when it is folded and shut) will have reference text #2 and our company contact information, plus any kind of stock photos, etc.
Nice to have
• Our main market will be first time investors, so we need to display and demonstrate relationships, and trust. We would prefer stock photos that incorporate families, children, or other images that solidify peace of mind.

```html
<!DOCTYPE html>
<html lang="en">
<head>
<meta charset="utf-8">
<title>Corvalink Property Management – Tri-fold Brochure</title>
<link href="https://fonts.googleapis.com/css2?family=Montserrat:wght@500;700;800&family=Roboto:wght@400;500&family=Roboto+Condensed:wght@700&family=Oswald:wght@500&display=swap" rel="stylesheet">
<style>
  :root{
    --blue:#1b8fd2;
    --ink:#151515;
    --panel-dark:#131313;
    --paper:#f6f6f6;
    --body:#3a3a3a;
    --muted:#cfcfcf;
    --bg:#d9d9d9;
    --seal:#c9a13a;
  }
  *{box-sizing:border-box;margin:0;padding:0}
  html,body{width:837px;height:1200px;overflow:hidden;background:var(--bg)}
  body{position:relative;font-family:"Roboto",sans-serif}
  .spread{position:absolute;left:18px;top:289px;width:829px;height:644px;transform:scale(0.965);transform-origin:0 0;background:var(--panel-dark);box-shadow:0 6px 18px rgba(0,0,0,.25)}

  /* ---------- inside-flap panel (light) ---------- */
  .panel-info{position:absolute;left:0;top:0;width:275px;height:644px;background:var(--paper)}
  .panel-info .edge{position:absolute;left:0;top:0;width:9px;height:644px;background:var(--blue)}
  .panel-info .topbar{position:absolute;left:0;top:0;width:145px;height:8px;background:var(--blue)}
  .info-col{position:absolute;left:41px;top:32px;width:204px}
  .section{position:relative;margin-bottom:14px}
  .section h2{font-family:"Montserrat",sans-serif;font-weight:800;font-size:13px;line-height:17px;color:var(--ink);letter-spacing:.2px}
  .section .icon{position:absolute;right:-6px;top:-8px;width:44px;height:40px}
  .wave{display:block;width:38px;height:6px;margin:5px 0 9px}
  .section p,.section li{font-size:7.3px;line-height:10.4px;color:var(--body)}
  .section p+p{margin-top:9px}
  .section ul{list-style:none;margin:1px 0 0 0}
  .section li::before{content:"• ";margin-left:2px}
  .info-url{position:absolute;left:33px;top:606px;font-size:10px;color:var(--ink)}

  /* ---------- middle panel ---------- */
  .panel-about{position:absolute;left:275px;top:0;width:272px;height:644px;background:var(--panel-dark)}
  .panel-about .top-rule{position:absolute;left:128px;top:0;width:144px;height:6px;background:var(--blue)}
  .panel-about .side-rule{position:absolute;right:0;top:0;width:8px;height:330px;background:var(--blue)}
  .panel-about .bottom-rule{position:absolute;left:128px;bottom:0;width:136px;height:7px;background:var(--blue)}
  .tab{position:absolute;left:19px;top:22px;width:38px;height:265px;background:var(--blue);clip-path:polygon(0 0,100% 0,100% 100%,50% 96%,0 100%)}
  .tab span{position:absolute;left:50%;top:50%;width:250px;transform:translate(-50%,-50%) rotate(-90deg);font-family:"Roboto Condensed",sans-serif;font-weight:700;font-size:11.5px;line-height:13px;color:#fff;text-align:center}
  .about-text{position:absolute;left:78px;top:50px;width:170px;color:#eaeaea;font-size:8.7px;line-height:16.4px}
  .about-text p+p{margin-top:16px}
  .contact-title{position:absolute;left:0;width:272px;top:316px;text-align:center;font-family:"Montserrat",sans-serif;font-weight:800;font-size:19px;letter-spacing:1.5px;color:var(--blue)}
  .contact-wave{position:absolute;left:117px;top:343px}
  .contact-icons{position:absolute;left:47px;top:372px;display:flex;gap:7px}
  .contact-icons svg{width:37px;height:37px}
  .address{position:absolute;left:0;width:272px;top:418px;text-align:center;color:#eee;font-size:8.3px;line-height:14.5px}
  .logo-box{position:absolute;left:47px;top:512px;width:174px;height:87px;border:1px solid #1f5f88;background:#0e0e0e;display:flex;flex-direction:column;align-items:center;justify-content:center;gap:7px}
  .logo-box .wordmark{font-size:9.5px;letter-spacing:1px}

  /* wordmark */
  .mark-square{width:18px;height:18px;background:var(--blue)}
  .wordmark{font-family:"Montserrat",sans-serif;font-weight:700;color:var(--blue);text-align:center;letter-spacing:1.5px;line-height:1.2;white-space:nowrap}

  /* ---------- cover panel ---------- */
  .panel-cover{position:absolute;left:547px;top:0;width:282px;height:644px;background:var(--panel-dark)}
  .cover-brand{position:absolute;left:0;top:24px;width:282px;display:flex;flex-direction:column;align-items:center;gap:9px}
  .cover-brand .mark-square{width:34px;height:34px}
  .cover-brand .wordmark{font-size:16px}
  .cover-wave{position:absolute;left:122px;top:122px}
  .cover-photo{position:absolute;left:0;top:140px;width:282px;height:310px;background:linear-gradient(160deg,#eef0f3 0%,#c9d6e4 45%,#8ea7c4 75%,#d4d0cc 100%)}
  .url-band{position:absolute;left:0;top:453px;width:282px;height:30px;background:var(--blue);color:#fff;font-size:10.5px;text-align:center;line-height:30px;letter-spacing:.2px}
  .contact-name{position:absolute;left:18px;top:508px;font-family:"Oswald",sans-serif;font-weight:500;font-size:21px;color:#fff;letter-spacing:.3px}
  .contact-role{position:absolute;left:18px;top:536px;font-size:14px;color:var(--blue)}
  .name-wave{position:absolute;left:18px;top:558px}
  .phones{position:absolute;left:18px;top:578px;font-family:"Roboto Condensed",sans-serif;font-weight:700;font-size:17.5px;line-height:21px;color:var(--blue)}
  .phones div{display:flex;align-items:center;gap:5px}
  .phones svg{width:10px;height:12px}
  .award-seal{position:absolute;left:172px;top:506px;width:90px;height:90px;border-radius:50%;background:var(--seal)}
</style>
</head>
<body>
<main class="spread">

  <section class="panel-info">
    <div class="edge"></div><div class="topbar"></div>
    <div class="info-col">
      <div class="section">
        <h2>OUR PORTFOLIO</h2>
        <svg class="wave" viewBox="0 0 38 6"><polyline points="0,5 3,1 6,5 9,1 12,5 15,1 18,5 21,1 24,5 27,1 30,5 33,1 36,5" fill="none" stroke="#1b8fd2" stroke-width="1.4"/></svg>
        <svg class="icon" viewBox="0 0 44 40"><rect x="3" y="12" width="38" height="25" fill="none" stroke="#cfcfcf" stroke-width="1.5"/><rect x="15" y="5" width="14" height="7" fill="none" stroke="#cfcfcf" stroke-width="1.5"/><line x1="3" y1="22" x2="41" y2="22" stroke="#cfcfcf" stroke-width="1.5"/><rect x="19" y="19" width="6" height="6" fill="#f6f6f6" stroke="#cfcfcf" stroke-width="1.5"/></svg>
        <p>Corvalink has distinguished itself as a leader in the management of smaller buildings: single family homes, duplexes, multi-unit buildings, smaller apartment blocks and single owner condominium units.</p>
        <p>Unlike large apartment blocks that give a rental discount to a caretaker to perform traditional property management duties, smaller buildings are more labour intensive and require a more "hands on" approach.</p>
        <p>Using the latest technology and specially trained field staff, Corvalink is able to efficiently manage your property.</p>
      </div>
      <div class="section">
        <h2>TENANT HAPPINESS<br>AND RETENTION</h2>
        <svg class="wave" viewBox="0 0 38 6"><polyline points="0,5 3,1 6,5 9,1 12,5 15,1 18,5 21,1 24,5 27,1 30,5 33,1 36,5" fill="none" stroke="#1b8fd2" stroke-width="1.4"/></svg>
        <svg class="icon" viewBox="0 0 44 40"><polyline points="4,19 22,4 40,19" fill="none" stroke="#cfcfcf" stroke-width="1.5"/><polyline points="9,15 9,37 35,37 35,15" fill="none" stroke="#cfcfcf" stroke-width="1.5"/><rect x="17" y="24" width="10" height="13" fill="none" stroke="#cfcfcf" stroke-width="1.5"/></svg>
        <p>At Corvalink, we believe we have two sets of clients: The Property Owner and the Tenant. A successful investment begins with finding a great tenant, but it doesn't end there!<br>We make a significant effort to keep tenants happy through:</p>
        <ul><li>Great Customer Service</li><li>Good communications</li><li>Tenant loyalty and retention programs</li></ul>
        <p style="margin-top:0">Creating happy tenants increase the likelihood they will sign their lease renewal, increasing the owners cashflow, reducing vacancies and minimizing turnover costs: A "Win-Win" for everyone involved.</p>
      </div>
      <div class="section">
        <h2>TRANSPARENCY<br>AND REPORTING</h2>
        <svg class="wave" viewBox="0 0 38 6"><polyline points="0,5 3,1 6,5 9,1 12,5 15,1 18,5 21,1 24,5 27,1 30,5 33,1 36,5" fill="none" stroke="#1b8fd2" stroke-width="1.4"/></svg>
        <svg class="icon" viewBox="0 0 44 40"><rect x="6" y="4" width="32" height="33" fill="none" stroke="#cfcfcf" stroke-width="1.5"/><rect x="11" y="10" width="10" height="9" fill="none" stroke="#cfcfcf" stroke-width="1.5"/><line x1="24" y1="12" x2="33" y2="12" stroke="#cfcfcf" stroke-width="1.5"/><line x1="24" y1="17" x2="33" y2="17" stroke="#cfcfcf" stroke-width="1.5"/><line x1="11" y1="24" x2="33" y2="24" stroke="#cfcfcf" stroke-width="1.5"/><line x1="11" y1="30" x2="33" y2="30" stroke="#cfcfcf" stroke-width="1.5"/></svg>
        <p>One of the biggest sources of stress to an owner using a property management company is the "unknown".<br>At Corvalink we go to great lengths to ensure there are no surprises. We ask your permission prior to sending out a contractor to repair an issue (except emergencies, of course) and our state-of-the-art maintenance system will keep you, and your tenant updated every step of the way. We give you access to an online portal so you can view your property's information anytime, but also send you a complete set of financial reports on a monthly basis.</p>
      </div>
    </div>
    <div class="info-url">www.corvalinkrent.net</div>
  </section>

  <section class="panel-about">
    <div class="top-rule"></div><div class="side-rule"></div><div class="bottom-rule"></div>
    <div class="tab"><span>WHY CHOOSE CORVALINK AS YOUR<br>PROPERTY MANAGEMENT COMPANY</span></div>
    <div class="about-text">
      <p>Corvalink has been recognized and voted multiple times as Riverton's Best Property Management Company by Harbor Tenant Medals. We are intently focussed on serving both owners and tenants and are dedicated to a culture of superior customer service.</p>
      <p>Whether you own one investment property or ten, the partnership process with Corvalink Property Management is easy, efficient and rewarding.</p>
    </div>
    <h2 class="contact-title">CONTACT US</h2>
    <svg class="contact-wave" width="38" height="6" viewBox="0 0 38 6"><polyline points="0,5 3,1 6,5 9,1 12,5 15,1 18,5 21,1 24,5 27,1 30,5 33,1 36,5" fill="none" stroke="#555" stroke-width="1.4"/></svg>
    <div class="contact-icons">
      <svg viewBox="0 0 37 37"><circle cx="18.5" cy="18.5" r="18" fill="#2b2b2b" stroke="#444"/><polyline points="11,18 18.5,11 26,18" fill="none" stroke="#ddd" stroke-width="1.4"/><polyline points="13,17 13,26 24,26 24,17" fill="none" stroke="#ddd" stroke-width="1.4"/></svg>
      <svg viewBox="0 0 37 37"><circle cx="18.5" cy="18.5" r="18" fill="#2b2b2b" stroke="#444"/><rect x="14" y="10" width="9" height="17" rx="1.5" fill="none" stroke="#ddd" stroke-width="1.4"/><line x1="17" y1="24" x2="20" y2="24" stroke="#ddd" stroke-width="1.4"/></svg>
      <svg viewBox="0 0 37 37"><circle cx="18.5" cy="18.5" r="18" fill="#2b2b2b" stroke="#444"/><path d="M12 12c0 8 5 13 13 13l1-4-4-2-2 2c-2-1-4-3-5-5l2-2-2-4z" fill="none" stroke="#ddd" stroke-width="1.4" stroke-linejoin="round"/></svg>
      <svg viewBox="0 0 37 37"><circle cx="18.5" cy="18.5" r="18" fill="#2b2b2b" stroke="#444"/><rect x="11" y="13" width="15" height="11" fill="none" stroke="#ddd" stroke-width="1.4"/><polyline points="11,13 18.5,19 26,13" fill="none" stroke="#ddd" stroke-width="1.4"/></svg>
    </div>
    <div class="address">C-214 Larchmont Ave, Riverton,<br>Ontario K2P 3H7<br>555-210-4400 &nbsp;|&nbsp; 555-210-4469<br>dana.pruitt@corvalinkrent.net</div>
    <div class="logo-box">
      <div class="mark-square" aria-hidden="true"></div>
      <div class="wordmark">CORVALINK<br>PROPERTY MANAGEMENT</div>
    </div>
  </section>

  <section class="panel-cover">
    <div class="cover-brand">
      <div class="mark-square" aria-hidden="true"></div>
      <div class="wordmark">CORVALINK<br>PROPERTY MANAGEMENT</div>
    </div>
    <svg class="cover-wave" width="38" height="6" viewBox="0 0 38 6"><polyline points="0,5 3,1 6,5 9,1 12,5 15,1 18,5 21,1 24,5 27,1 30,5 33,1 36,5" fill="none" stroke="#555" stroke-width="1.4"/></svg>
    <div class="cover-photo" role="img" aria-label="Photo of a smiling young family sitting together on the floor of a bright home, the child holding a potted plant"></div>
    <div class="url-band">www.corvalinkrent.net</div>
    <div class="contact-name">DANA PRUITT</div>
    <div class="contact-role">President</div>
    <svg class="name-wave" width="38" height="6" viewBox="0 0 38 6"><polyline points="0,5 3,1 6,5 9,1 12,5 15,1 18,5 21,1 24,5 27,1 30,5 33,1 36,5" fill="none" stroke="#555" stroke-width="1.4"/></svg>
    <div class="phones">
      <div><svg viewBox="0 0 10 12"><rect x="1.5" y="0.7" width="7" height="10.6" rx="1" fill="none" stroke="#fff" stroke-width="1.2"/></svg>555-210-4400</div>
      <div><svg viewBox="0 0 10 12"><path d="M1 4h8v7H1z M0 4c2-3 8-3 10 0" fill="#fff"/></svg>555-210-4469</div>
    </div>
    <div class="award-seal" role="img" aria-label="Harbor Tenant Medals award badge"></div>
  </section>

</main>
</body>
</html>
```